SEO AND WEB DESIGN COMPANY BUSINESS CARD DESIGN

I need an eye catching , simple business card design that will match my logo . I need 2 versions of it ( white background and black background) - SOME PEOPLE DID NOT GET IT AND SENDING US FRONT WHITE BACK WHITE VERSIONS WHICH IS NOT CORRECT.

ONE VERSION SHOULD BE BACK AND FRONT ALL BLACK , SECOND VERSION SHOULD BE BACK AND FRONT ALL WHITE

logo psd files are attached for both versions. The business card is going to have : First Name- Last name - position - phone numbers

```html
<!DOCTYPE html>
<html lang="en">
<head>
<meta charset="utf-8">
<title>Lumen Digital – Business Card</title>
<link rel="stylesheet" href="https://fonts.googleapis.com/css2?family=Oswald:wght@500&family=Source+Sans+3:wght@400&family=Jost:wght@300&display=swap">
<style>
  :root {
    --page-bg: #e8e5e1;
    --card-bg: #ffffff;
    --ink: #111418;
    --ink-soft: #2a2d31;
    --accent: #3f8fd2;
    --card-shadow: 0 6px 18px rgba(0, 0, 0, 0.18);
  }
  * { margin: 0; padding: 0; box-sizing: border-box; }
  html, body {
    width: 1200px;
    height: 960px;
    overflow: hidden;
    background: var(--page-bg);
  }
  .canvas {
    position: relative;
    width: 1200px;
    height: 960px;
  }
  .card {
    position: absolute;
    left: 273px;
    width: 660px;
    height: 391px;
    background: var(--card-bg);
    box-shadow: var(--card-shadow);
    overflow: hidden;
  }
  .card--front { top: 99px; }
  .card--back { top: 513px; }

  .brand {
    position: absolute;
    inset: 0;
    display: flex;
    align-items: center;
    justify-content: center;
    gap: 14px;
  }
  .brand__dot {
    width: 30px;
    height: 30px;
    border-radius: 50%;
    background: var(--accent);
  }
  .brand__name {
    font-family: "Oswald", sans-serif;
    font-weight: 500;
    font-size: 64px;
    letter-spacing: 1px;
    color: var(--ink);
    line-height: 1;
  }

  .back-mark {
    position: absolute;
    left: 0;
    top: 0;
  }
  .holder__name {
    position: absolute;
    right: 112px;
    top: 56px;
    font-family: "Source Sans 3", sans-serif;
    font-weight: 400;
    font-size: 35px;
    color: var(--ink-soft);
    line-height: 1;
  }
  .holder__rule {
    position: absolute;
    left: 398px;
    right: 0;
    top: 98px;
    height: 3px;
    background: linear-gradient(90deg, rgba(63, 143, 210, 0.2), var(--accent) 25%);
  }
  .holder__role {
    position: absolute;
    right: 112px;
    top: 106px;
    font-family: "Source Sans 3", sans-serif;
    font-size: 20px;
    color: var(--ink-soft);
    line-height: 1;
  }
  .contact {
    position: absolute;
    left: 379px;
    top: 253px;
    list-style: none;
    font-family: "Jost", sans-serif;
    font-weight: 300;
    font-size: 23px;
    color: var(--ink-soft);
    line-height: 30px;
  }
</style>
</head>
<body>
<main class="canvas">
  <section class="card card--front" aria-label="Card front">
    <div class="brand">
      <span class="brand__dot"></span>
      <span class="brand__name">LUMEN DIGITAL</span>
    </div>
  </section>

  <section class="card card--back" aria-label="Card back">
    <svg class="back-mark" width="660" height="391" viewBox="0 0 660 391" aria-hidden="true">
      <circle cx="158" cy="219" r="112" fill="none" stroke="var(--accent)" stroke-width="22"/>
    </svg>
    <h1 class="holder__name">Daniel Moreau</h1>
    <div class="holder__rule"></div>
    <p class="holder__role">President</p>
    <ul class="contact">
      <li>phone: (xx) xxx-xxxxx</li>
      <li>phone: (xx) xxx-xxxxx</li>
    </ul>
  </section>
</main>
</body>
</html>
```